Report Design

I am looking for a redesign of our monthly inspection reports we submit to our customers. I uploaded the current one we use (Tallowfern) and also that of a competitor (Cedar Knoll). I want to more copy the layout of the Cedarknoll report I attached but with more flow and design.

Requirements
Must have
• This has to be in a template format that we can modify the content every month.

```html
<!DOCTYPE html>
<html lang="en">
<head>
<meta charset="utf-8">
<title>Quality Site Assessment</title>
<link href="https://fonts.googleapis.com/css2?family=Oswald:wght@400;500&family=Open+Sans:wght@400;600;700&family=Bebas+Neue&display=swap" rel="stylesheet">
<style>
:root{
  --green:#74a92c;
  --green-light:#8dc63f;
  --blue:#1a73c9;
  --blue-deep:#1565b8;
  --ink:#333a40;
  --rule:#9aa3aa;
  --grey:#e4e6e8;
  --stage:#424242;
  --white:#ffffff;
}
*{margin:0;padding:0;box-sizing:border-box}
html,body{width:857px;height:1200px;overflow:hidden;background:var(--stage)}
.stage{position:relative;width:857px;height:1200px;background:var(--stage)}
.page{position:absolute;top:316px;width:664px;height:940px;background:var(--white);transform:scale(.605);transform-origin:0 0;font-family:"Open Sans",sans-serif;color:var(--ink);box-shadow:0 10px 30px rgba(0,0,0,.45);overflow:hidden}
.page-summary{left:18px}
.page-photos{left:438px}
.page-shapes{position:absolute;left:0;top:0}

/* summary page */
.summary-title{position:absolute;left:40px;top:28px;font-family:"Bebas Neue",sans-serif;font-weight:400;font-size:34px;letter-spacing:.3px;color:var(--white);line-height:40px}
.site-details{position:absolute;left:42px;top:98px;list-style:none;font-family:"Oswald",sans-serif;font-size:13.5px;line-height:24.5px;color:var(--ink)}
.site-details b{color:var(--blue);font-weight:500}
.focus-label{position:absolute;left:64px;top:231px;font-weight:700;font-size:14px;line-height:20px;color:var(--white)}
.focus-text{position:absolute;left:42px;top:264px;width:330px;font-size:15.5px;line-height:21.5px;color:var(--white)}
.column{position:absolute;top:356px}
.column-left{left:40px;width:280px}
.column-right{left:348px;width:285px}
.column h2{font-size:14.5px;font-weight:600;color:var(--blue);line-height:21px}
.items{list-style:none;position:relative;margin-top:9px}
.items::before{content:"";position:absolute;left:7px;top:6px;bottom:10px;border-left:1px solid var(--rule)}
.items li{position:relative;padding-left:30px;font-size:9.6px;line-height:13.5px;margin-bottom:4.5px}
.items li span{position:absolute;left:0;top:0;width:14px;height:14px;border-radius:50%;background:var(--green);color:var(--white);font-size:8px;font-weight:700;line-height:14px;text-align:center;box-shadow:0 0 0 2px var(--white)}
.column-right .items{margin-top:10px}
.column-right .items li{margin-bottom:6px}
.notes-label{position:absolute;left:48px;top:762px;font-weight:700;font-size:14px;line-height:20px;color:var(--white)}

/* photo page */
.photos-title{position:absolute;left:157px;top:42px;width:345px;height:40px;text-align:center;font-family:"Bebas Neue",sans-serif;font-size:30px;line-height:42px;color:var(--white)}
.panel{position:absolute;width:270px}
.panel h2{font-size:14.5px;font-weight:600;line-height:20px;color:var(--blue)}
.panel p{margin-top:5px;font-size:12.8px;line-height:18px;color:var(--ink)}
.panel-dark h2{color:var(--green-light)}
.panel-dark p{color:var(--white)}
.panel-a{left:42px;top:108px}
.panel-b{left:345px;top:108px}
.panel-c{left:42px;top:470px}
.panel-d{left:345px;top:470px}

/* footer */
.page-footer{position:absolute;left:42px;right:42px;top:880px;display:flex;align-items:center;font-size:19px;line-height:26px;color:var(--ink)}
.page-footer .sep{width:1px;height:24px;background:#777;margin:0 24px}
.page-footer .phone,.page-footer .web{display:flex;align-items:center;gap:9px}
.brand{margin-left:auto;display:flex;align-items:center;gap:7px;font-weight:700;font-size:20px;color:var(--blue)}
.brand i{width:10px;height:10px;background:var(--green);display:block}
</style>
</head>
<body>
<div class="stage">

  <article class="page page-summary">
    <svg class="page-shapes" width="664" height="940" viewBox="0 0 664 940">
      <defs>
        <linearGradient id="crewTone" x1="0" y1="0" x2="1" y2="1">
          <stop offset="0" stop-color="#c9d4de"/>
          <stop offset=".45" stop-color="#ece6de"/>
          <stop offset=".75" stop-color="#f3a05a"/>
          <stop offset="1" stop-color="#d8dde2"/>
        </linearGradient>
      </defs>
      <polygon points="0,0 430,0 340,88 0,88" fill="var(--green)"/>
      <rect x="0" y="240" width="664" height="100" fill="var(--blue)"/>
      <polygon points="40,228 290,228 305,252 40,252" fill="var(--green)"/>
      <polygon points="428,0 664,0 664,212 473,338 293,132" fill="var(--white)" stroke="var(--green)" stroke-width="4"/>
      <polygon points="437,0 664,0 664,203 473,326 306,132" fill="url(#crewTone)" role="img" aria-label="Photo of two site inspectors in hard hats reviewing plans"/>
      <polygon points="600,0 664,0 664,60" fill="var(--green)"/>
      <polygon points="40,760 262,760 276,784 40,784" fill="var(--blue)"/>
      <polyline points="270,762 325,797 664,797" fill="none" stroke="var(--grey)" stroke-width="3"/>
      <line x1="40" y1="868" x2="615" y2="868" stroke="var(--green)" stroke-width="1.5"/>
    </svg>

    <h1 class="summary-title">QUALITY SITE ASSESSMENT</h1>

    <ul class="site-details">
      <li><b>PROPERTY NAME:</b> St Aldhelm Priory(5810-96622)</li>
      <li><b>DATE:</b> Tuesday, February 02, 2021</li>
      <li><b>NEXT INSPECTION DATE:</b> Tuesday, March 02, 2021</li>
      <li><b>CLIENT ATTENDEES:</b> Sister Agnes</li>
      <li><b>CEDAR KNOLL ATTENDEES:</b> Marcus Penrow, Daniel Ashcombe</li>
    </ul>

    <p class="focus-label">CUSTOMER FOCUS AREA:</p>
    <p class="focus-text">Weed free beds, plant separation, tree trimming, checking irrigation frequently, mowing pond when dry.</p>

    <section class="column column-left">
      <h2>MAINTENANCE ITEMS:</h2>
      <ol class="items">
        <li><span>1</span>Maintenance crew will flush cut palm growing along side oak located in back of convent.</li>
        <li><span>2</span>Maintenance crew will trim Palm located in back of convent next visit.</li>
        <li><span>3</span>Maintenance crew will blow leaves away from building next visit. During the colder months we work on removing leaves instead of mowing.</li>
        <li><span>4</span>It has been confirmed that this downspout has contributed to this hole holding water. There is no where for it to drain. Irrigation was turned off last inspection.</li>
        <li><span>5</span>Maintenance crew will not trim azaleas until they are done blooming. This will occur in April.</li>
        <li><span>6</span>Maintenance crew will remove any trash during the next visit,</li>
        <li><span>7</span>Maintenance crew will trim the declining yellowing leaves off the crinum next visit.</li>
        <li><span>8</span>Maintenance crew will hand prune ginger of sidewalks.</li>
        <li><span>9</span>This division in leaves is caused by roof water run off. No gutters in this area.</li>
        <li><span>10</span>Maintenance crew will work on removing leaves from front entrance next visit.</li>
      </ol>
    </section>

    <section class="column column-right">
      <h2>RECOMMENDATIONS FOR PROPERTY ENHANCEMENTS:</h2>
      <ol class="items">
        <li><span>1</span>Fallen tree branch located in back of property will be included in our tree proposal for this year.</li>
        <li><span>2</span>We recommend filling in landscape areas after our tree work is completed this year.</li>
        <li><span>3</span>We recommend upgrading fences around property. They are failing in many areas.</li>
        <li><span>4</span>Dead tree located in pool area will be included in tree proposal.</li>
        <li><span>5</span>Reducing this viburnum by 75% will be in our tree proposal as well.</li>
        <li><span>6</span>Another area for enhancements located in front parking area. Sister were requesting annuals for spring. To be revisited in April.</li>
        <li><span>7</span>We recommend replacing crotons with a more vibrant arbicola to brighten up area.</li>
        <li><span>8</span>) Laurel oak with ganoderma will be included in tree proposals.</li>
        <li><span>9</span>Another declining Laurel will also be included in tree proposal.</li>
        <li><span>10</span>After removals have been completed we will recommend sodding area with new turf.</li>
      </ol>
    </section>

    <p class="notes-label">NOTES TO OWNER/CLIENT:</p>

    <footer class="page-footer">
      <span class="phone"><svg width="15" height="15" viewBox="0 0 24 24" aria-hidden="true"><path d="M6.6 10.8a15 15 0 0 0 6.6 6.6l2.2-2.2a1 1 0 0 1 1-.25 11.4 11.4 0 0 0 3.6.57 1 1 0 0 1 1 1V20a1 1 0 0 1-1 1A17 17 0 0 1 3 4a1 1 0 0 1 1-1h3.5a1 1 0 0 1 1 1c0 1.25.2 2.45.57 3.57a1 1 0 0 1-.25 1z" fill="var(--green)"/></svg>555.014.0287</span>
      <span class="sep"></span>
      <span class="web"><svg width="14" height="14" viewBox="0 0 24 24" aria-hidden="true"><circle cx="12" cy="12" r="10" fill="none" stroke="var(--green)" stroke-width="3"/><path d="M2 12h20M12 2c3 3 3 17 0 20M12 2c-3 3-3 17 0 20" stroke="var(--green)" stroke-width="2" fill="none"/></svg>cedarknoll.com</span>
      <span class="sep"></span>
      <span class="brand">Cedar Knoll<i></i></span>
    </footer>
  </article>

  <article class="page page-photos">
    <svg class="page-shapes" width="664" height="940" viewBox="0 0 664 940">
      <defs>
        <linearGradient id="palmTone" x1="0" y1="0" x2="1" y2="1">
          <stop offset="0" stop-color="#4f5e3a"/>
          <stop offset=".5" stop-color="#6e5a42"/>
          <stop offset="1" stop-color="#a89274"/>
        </linearGradient>
        <linearGradient id="bedTone" x1="0" y1="0" x2="1" y2="1">
          <stop offset="0" stop-color="#d9dcdc"/>
          <stop offset=".5" stop-color="#7a6048"/>
          <stop offset="1" stop-color="#3f5b2f"/>
        </linearGradient>
        <linearGradient id="puddleTone" x1="0" y1="0" x2="0" y2="1">
          <stop offset="0" stop-color="#b9b4ac"/>
          <stop offset=".5" stop-color="#7e6a55"/>
          <stop offset="1" stop-color="#a39886"/>
        </linearGradient>
      </defs>
      <rect x="0" y="60" width="664" height="4" fill="var(--blue)"/>
      <rect x="157" y="42" width="345" height="40" rx="20" fill="var(--green)"/>
      <line x1="328" y1="112" x2="328" y2="432" stroke="var(--green)" stroke-width="1.2" stroke-dasharray="2 3"/>
      <rect x="41" y="202" width="266" height="229" fill="var(--white)" stroke="var(--green)" stroke-width="3"/>
      <rect x="46" y="207" width="256" height="219" fill="url(#palmTone)" role="img" aria-label="Photo of a cut palm growing beside an oak trunk"/>
      <rect x="349" y="202" width="266" height="229" fill="var(--white)" stroke="var(--green)" stroke-width="3"/>
      <rect x="354" y="207" width="256" height="219" fill="url(#palmTone)" role="img" aria-label="Photo of a palm with dry hanging fronds behind the convent"/>
      <rect x="0" y="452" width="664" height="393" fill="var(--blue-deep)"/>
      <line x1="328" y1="472" x2="328" y2="820" stroke="var(--green-light)" stroke-width="1.2" stroke-dasharray="2 3"/>
      <rect x="41" y="585" width="266" height="232" fill="var(--white)" stroke="var(--green)" stroke-width="3"/>
      <rect x="46" y="590" width="256" height="222" fill="url(#bedTone)" role="img" aria-label="Photo of a mulched bed covered in leaves beside a building"/>
      <rect x="349" y="585" width="266" height="232" fill="var(--white)" stroke="var(--green)" stroke-width="3"/>
      <rect x="354" y="590" width="256" height="222" fill="url(#puddleTone)" role="img" aria-label="Photo of a downspout and a hole holding water"/>
      <line x1="40" y1="868" x2="615" y2="868" stroke="var(--green)" stroke-width="1.5"/>
    </svg>

    <h1 class="photos-title">QUALITY SITE ASSESSMENT</h1>

    <section class="panel panel-a">
      <h2>MAINTENANCE ITEMS</h2>
      <p>Maintenance crew will flush cut palm growing along side oak located in back of convent.</p>
    </section>
    <section class="panel panel-b">
      <h2>MAINTENANCE ITEMS</h2>
      <p>Maintenance crew will trim Palm located in back of convent next visit.</p>
    </section>
    <section class="panel panel-dark panel-c">
      <h2>MAINTENANCE ITEMS</h2>
      <p>Maintenance crew will blow leaves away from building next visit. During the colder months we work on removing leaves instead of mowing.</p>
    </section>
    <section class="panel panel-dark panel-d">
      <h2>MAINTENANCE ITEMS</h2>
      <p>It has been confirmed that this downspout has contributed to this hole holding water. There is no where for it to drain. Irrigation was turned off last inspection.</p>
    </section>

    <footer class="page-footer">
      <span class="phone"><svg width="15" height="15" viewBox="0 0 24 24" aria-hidden="true"><path d="M6.6 10.8a15 15 0 0 0 6.6 6.6l2.2-2.2a1 1 0 0 1 1-.25 11.4 11.4 0 0 0 3.6.57 1 1 0 0 1 1 1V20a1 1 0 0 1-1 1A17 17 0 0 1 3 4a1 1 0 0 1 1-1h3.5a1 1 0 0 1 1 1c0 1.25.2 2.45.57 3.57a1 1 0 0 1-.25 1z" fill="var(--green)"/></svg>555.014.0287</span>
      <span class="sep"></span>
      <span class="web"><svg width="14" height="14" viewBox="0 0 24 24" aria-hidden="true"><circle cx="12" cy="12" r="10" fill="none" stroke="var(--green)" stroke-width="3"/><path d="M2 12h20M12 2c3 3 3 17 0 20M12 2c-3 3-3 17 0 20" stroke="var(--green)" stroke-width="2" fill="none"/></svg>cedarknoll.com</span>
      <span class="sep"></span>
      <span class="brand">Cedar Knoll<i></i></span>
    </footer>
  </article>

</div>
</body>
</html>
```